Business Cards Needed For Veterinary Business

Looking for a business card design for a veterinary blood bank. We would like it to be clean and professional on appearance but still warm and inviting. We would like to utilize our logo and similar coloring. We will use our phone number, email, website, employee name, employee title.

We do not want a bunch of animated animal photos but do not need the style to be as clinical as a laboratory or human medical procedure office.

We are looking for some creative ideas to choose from so that we can generate a standout professional business card for our management team to utilize.

Target Market(s)

professionals

Industry/Entity Type

veterinary

Contact Information for Business Card

employee name, employee title, phone number, website URL, email

Font styles to use
Sans Serif

Colors
0054AA
0677BA
7BADD7
CADEEF
E8F1F8
EB3D1F
EC4F4E
F09395
F8D3D4
FCEDEE

Requirements
Nice to have
• creative design
Should not have
• animated photos

```html
<!DOCTYPE html>
<html lang="en">
<head>
<meta charset="utf-8">
<title>Pawline Blood Bank – Business Card</title>
<link href="https://fonts.googleapis.com/css2?family=Montserrat:wght@400;500;800&display=swap" rel="stylesheet">
<style>
  :root {
    --blue: #0054aa;
    --blue-deep: #0d4f94;
    --red: #eb3d1f;
    --red-deep: #c8233a;
    --ink: #2a2a2a;
    --rule: #b9bfd0;
    --paper: #ffffff;
    --stage: #2e2e30;
  }
  * { margin: 0; padding: 0; box-sizing: border-box; }
  html, body { width: 1200px; height: 866px; overflow: hidden; }
  body {
    background: var(--stage);
    font-family: "Montserrat", Arial, sans-serif;
    display: flex; align-items: center; justify-content: center; gap: 40px;
  }
  .card {
    position: relative; width: 540px; height: 309px; overflow: hidden;
    box-shadow: 0 10px 24px rgba(0,0,0,.45);
  }
  /* front */
  .card-front { background: var(--paper); }
  .contact { position: absolute; left: 34px; top: 92px; width: 230px; }
  .contact-name { color: var(--red); font-weight: 800; font-size: 19px; letter-spacing: .5px; text-transform: uppercase; }
  .contact-title { color: var(--ink); font-size: 13px; font-weight: 500; margin-top: 2px; letter-spacing: .4px; }
  .contact-rule { height: 1px; background: var(--rule); margin: 10px 0 10px; }
  .contact-line { display: flex; align-items: center; gap: 8px; color: var(--ink); font-size: 12.5px; letter-spacing: .4px; margin-bottom: 5px; }
  .contact-line svg { flex: none; }
  .brand { position: absolute; right: 34px; top: 108px; display: flex; align-items: center; gap: 10px; }
  .brand-dot { width: 26px; height: 26px; border-radius: 50%; background: var(--red); }
  .brand-name { font-weight: 800; font-size: 24px; color: var(--blue); letter-spacing: .3px; line-height: 1.05; }
  .long-rule { position: absolute; left: 280px; right: 40px; top: 232px; height: 1px; background: var(--rule); }
  .card-bands { position: absolute; left: 0; bottom: 0; }
  .website { position: absolute; right: 40px; bottom: 10px; color: #fff; font-size: 13px; letter-spacing: 1px; }
  /* back */
  .card-back {
    background: linear-gradient(215deg, var(--red-deep) 0%, #5a3a72 40%, var(--blue-deep) 72%);
    display: flex; align-items: center; justify-content: center;
  }
  .card-back .brand { position: static; }
  .card-back .brand-name { color: #fff; font-size: 34px; }
  .card-back .brand-dot { width: 34px; height: 34px; background: #fff; }
</style>
</head>
<body>
  <section class="card card-front" aria-label="Business card front">
    <div class="contact">
      <p class="contact-name">Daniel Reyes</p>
      <p class="contact-title">Managing Director</p>
      <div class="contact-rule"></div>
      <p class="contact-line">
        <svg width="13" height="13" viewBox="0 0 24 24" aria-hidden="true"><path fill="#eb3d1f" d="M6.6 10.8a15 15 0 0 0 6.6 6.6l2.2-2.2c.3-.3.7-.4 1-.2 1.1.4 2.3.6 3.6.6.6 0 1 .4 1 1V20c0 .6-.4 1-1 1A17 17 0 0 1 3 4c0-.6.4-1 1-1h3.5c.6 0 1 .4 1 1 0 1.3.2 2.5.6 3.6.1.3 0 .7-.2 1z"/></svg>
        044-555 010 227
      </p>
      <p class="contact-line">
        <svg width="13" height="11" viewBox="0 0 24 18" aria-hidden="true"><rect width="24" height="18" rx="2" fill="#eb3d1f"/><path d="M1 2l11 8 11-8" stroke="#fff" stroke-width="2" fill="none"/></svg>
        hello@pawline.org
      </p>
    </div>
    <div class="brand">
      <span class="brand-dot"></span>
      <span class="brand-name">Pawline<br>Blood Bank</span>
    </div>
    <div class="long-rule"></div>
    <svg class="card-bands" width="540" height="60" viewBox="0 0 540 60" aria-hidden="true">
      <path d="M0 30 L200 30 L205 34 L0 34 Z" fill="#eb3d1f"/>
      <path d="M0 38 L200 38 C228 38 226 22 258 22 L540 22 L540 60 L0 60 Z" fill="#0054aa"/>
    </svg>
    <p class="website">www.pawline.org</p>
  </section>

  <section class="card card-back" aria-label="Business card back">
    <div class="brand">
      <span class="brand-dot"></span>
      <span class="brand-name">Pawline<br>Blood Bank</span>
    </div>
  </section>
</body>
</html>
```